Talvok Engineering Business card Design

We need to make business cards for our NDT and inspection company. The company is called Talvok Engineering. We want a professional modern feel business card. We have just completed the remaking of our website and would like to have business cards with the same feel and colours. The final design should communicate professionalism and cutting edge tech.

Target Market(s)

We sell to B2B Business clients. Our customer is an engineer or decision maker in the mechanical engineering / Oil and gas field.

Contact Information for Business Card

Please see the current business cards that we have uploaded to get the details. You can also look at our Website www.talvok-eng.example for more.

Requirements
Must have
• Less is more
Nice to have
• Less is more

```html
<!DOCTYPE html>
<html lang="en">
<head>
<meta charset="utf-8">
<title>Talvok Engineering – Business Card</title>
<link rel="stylesheet" href="https://fonts.googleapis.com/css2?family=Montserrat:wght@500;600;700&display=swap">
<style>
  :root {
    --navy: #253a6e;
    --navy-deep: #1d2f5c;
    --red: #b3242a;
    --red-deep: #a31e25;
    --white: #ffffff;
    --stage: #2b2b2d;
  }
  * { box-sizing: border-box; margin: 0; padding: 0; }
  html, body { width: 1200px; height: 900px; overflow: hidden; }
  body {
    background: var(--stage);
    font-family: "Montserrat", Arial, sans-serif;
    display: flex; flex-direction: column; align-items: center; justify-content: center;
    gap: 44px;
  }
  .card {
    position: relative; width: 660px; height: 377px; overflow: hidden;
    box-shadow: 0 14px 30px rgba(0,0,0,.45);
  }

  /* Front */
  .card--front { background: radial-gradient(circle at 40% 40%, #2c4278, var(--navy-deep)); color: var(--white); }
  .contact { position: absolute; right: 360px; top: 78px; text-align: right; }
  .contact__name { font-weight: 700; font-size: 20px; letter-spacing: .5px; margin-bottom: 18px; }
  .contact__row {
    display: flex; justify-content: flex-end; align-items: center; gap: 10px;
    font-size: 14.5px; font-weight: 500; line-height: 1.25; margin-bottom: 8px;
  }
  .contact__icon {
    width: 20px; height: 20px; border-radius: 50%; background: var(--red);
    display: inline-flex; align-items: center; justify-content: center; flex: none;
  }
  .contact__address { text-align: right; }
  .divider { position: absolute; left: 322px; top: 70px; width: 2px; height: 210px; background: var(--red); }
  .brand { position: absolute; left: 350px; top: 120px; display: flex; flex-direction: column; align-items: flex-start; gap: 14px; }
  .brand__mark { width: 70px; height: 70px; border-radius: 50%; background: var(--red); }
  .brand__name { font-weight: 600; font-size: 26px; letter-spacing: 1px; color: var(--white); line-height: 1.15; }
  .social { position: absolute; left: 420px; bottom: 34px; display: flex; align-items: center; gap: 8px; font-size: 13px; font-weight: 500; }
  .social__box { width: 18px; height: 18px; background: var(--red); border-radius: 2px; }

  /* Back */
  .card--back { background: var(--white); }
  .back__band {
    position: absolute; inset: 0;
    background: linear-gradient(100deg, var(--navy) 0%, #6a2c55 45%, var(--red) 75%, var(--red-deep) 100%);
    clip-path: polygon(0 22%, 52% 22%, 70% 46%, 100% 46%, 100% 100%, 0 100%);
  }
  .back__rule { position: absolute; left: 0; right: 0; bottom: 34px; height: 3px; background: var(--white); }
  .back__brand { position: absolute; right: 36px; top: 22px; display: flex; align-items: center; gap: 12px; }
  .back__mark { width: 50px; height: 50px; border-radius: 50%; background: var(--navy); }
  .back__name { font-weight: 600; font-size: 21px; color: var(--navy); letter-spacing: .8px; }
  .back__url { font-weight: 500; font-size: 11px; color: var(--navy); letter-spacing: 3px; margin-top: 3px; }
  .services { position: absolute; list-style: none; color: var(--white); font-weight: 600; font-size: 13px; line-height: 1.62; }
  .services li::before {
    content: ""; display: inline-block; width: 7px; height: 7px; background: var(--white); margin-right: 10px; vertical-align: 2px;
  }
  .services--inspections { left: 34px; top: 98px; }
  .services--ndt { left: 380px; top: 196px; }
</style>
</head>
<body>

<section class="card card--front" aria-label="Business card front">
  <div class="contact">
    <p class="contact__name">WEKESA, DANIEL OTIENO</p>
    <p class="contact__row">+254 20 555 0142/3
      <span class="contact__icon"><svg width="11" height="11" viewBox="0 0 24 24"><path fill="#fff" d="M6.6 10.8a15 15 0 0 0 6.6 6.6l2.2-2.2a1 1 0 0 1 1-.25 11.4 11.4 0 0 0 3.6.57 1 1 0 0 1 1 1V20a1 1 0 0 1-1 1A17 17 0 0 1 3 4a1 1 0 0 1 1-1h3.5a1 1 0 0 1 1 1c0 1.25.2 2.45.57 3.57a1 1 0 0 1-.25 1z"/></svg></span></p>
    <p class="contact__row">info@talvok-eng.example
      <span class="contact__icon"><svg width="11" height="11" viewBox="0 0 24 24"><path fill="#fff" d="M2 5h20v14H2zm2 2v.5l8 5 8-5V7z"/></svg></span></p>
    <p class="contact__row">www.talvok-eng.example
      <span class="contact__icon"><svg width="11" height="11" viewBox="0 0 24 24"><circle cx="12" cy="12" r="9" fill="none" stroke="#fff" stroke-width="2"/><path d="M3 12h18M12 3c3 3 3 15 0 18M12 3c-3 3-3 15 0 18" fill="none" stroke="#fff" stroke-width="1.6"/></svg></span></p>
    <p class="contact__row"><span class="contact__address">P.O. BOX 40577-80100<br>Mombasa Kenya</span>
      <span class="contact__icon"><svg width="11" height="11" viewBox="0 0 24 24"><path fill="#fff" d="M12 2a7 7 0 0 0-7 7c0 5 7 13 7 13s7-8 7-13a7 7 0 0 0-7-7zm0 9.5A2.5 2.5 0 1 1 12 6.5a2.5 2.5 0 0 1 0 5z"/></svg></span></p>
  </div>
  <div class="divider"></div>
  <div class="brand">
    <span class="brand__mark"></span>
    <span class="brand__name">TALVOK<br>ENGINEERING</span>
  </div>
  <div class="social">Find us on <span class="social__box"></span><span class="social__box"></span></div>
</section>

<section class="card card--back" aria-label="Business card back">
  <div class="back__band"></div>
  <div class="back__brand">
    <span class="back__mark"></span>
    <div>
      <p class="back__name">TALVOK ENGINEERING</p>
      <p class="back__url">WWW.TALVOK-ENG.EXAMPLE</p>
    </div>
  </div>
  <ul class="services services--inspections">
    <li>API 653 Tank Inspections</li>
    <li>API 570 Pipeline Inspections</li>
    <li>API 510 Pressure Vessel Inspections</li>
    <li>Welding Inspections</li>
    <li>Electrical Inspections</li>
    <li>OCTG Inspections</li>
    <li>Lifting Equipment Inspections</li>
  </ul>
  <ul class="services services--ndt">
    <li>Non-Destructive Testing</li>
    <li>UT / PT / MT / RT / VT</li>
    <li>Advanced NDT</li>
    <li>PAUT / MFL / ILI</li>
    <li>Engineering Projects</li>
  </ul>
  <div class="back__rule"></div>
</section>

</body>
</html>
```